flyer for letter box drop 2012

Advertising flyer that is delivered to homes in our suburb.
We are optometrists and looking to have a flyer delivered into our local area residential letterboxes. As a business that has been in the area for 25 years we are looking for an innovative approach to keeping our existing customers as well as appealing to the new generation.
We would like the flyer to reflect or professional eye care services
and commitment to quality service and products.
We do not promote our selves as a discount outlet for eg 2 for 1,50% of everything.
I have attached a copy of the flyer we have been using for the last 12 months.

Target Market(s)

25- 70 year olds male and female

Industry/Entity Type

Residential

Requirements
Must have
• flyer should be double sided a5 page
Prominent logo display
address ,phone number , web address,

```html
<!DOCTYPE html>
<html lang="en">
<head>
<meta charset="utf-8">
<title>Hadley Lane Optical – Frequently Asked Questions</title>
<link href="https://fonts.googleapis.com/css2?family=Arimo:wght@400;700&family=Roboto+Condensed:wght@700&display=swap" rel="stylesheet">
<style>
  :root {
    --navy: #2e3185;
    --green: #1fa24a;
    --ink: #2b2b2b;
    --paper: #ffffff;
  }
  html, body {
    margin: 0;
    padding: 0;
    width: 855px;
    height: 1200px;
    overflow: hidden;
    background: var(--paper);
  }
  .flyer {
    position: relative;
    width: 855px;
    height: 1200px;
    background: var(--paper);
    font-family: "Arimo", Arial, sans-serif;
    color: var(--ink);
    overflow: hidden;
  }
  .side-band {
    position: absolute;
    left: 81px;
    top: 0;
    width: 48px;
    height: 1200px;
    background: var(--navy);
  }
  .side-band__title {
    position: absolute;
    /* box is 508 x 48, rotated about its centre to sit along the band */
    left: -230px;
    top: 491px;
    width: 508px;
    height: 48px;
    margin: 0;
    transform: rotate(-90deg);
    transform-origin: 50% 50%;
    text-align: center;
    font-family: "Roboto Condensed", "Arial Narrow", sans-serif;
    font-weight: 700;
    font-size: 33px;
    line-height: 48px;
    letter-spacing: 0.4px;
    color: var(--paper);
    white-space: nowrap;
  }
  .tagline-bar {
    position: absolute;
    left: 0;
    top: 101px;
    width: 572px;
    height: 44px;
    background: var(--green);
    display: flex;
    align-items: center;
  }
  .tagline-bar__text {
    margin: 0 0 0 60px;
    font-size: 18px;
    color: var(--paper);
    white-space: nowrap;
  }
  .corner-block {
    position: absolute;
    left: 808px;
    top: 101px;
    width: 47px;
    height: 44px;
    background: var(--green);
  }
  .brand-name {
    position: absolute;
    left: 590px;
    top: 82px;
    width: 210px;
    text-align: center;
    font-weight: 400;
    color: var(--navy);
    font-size: 27px;
    line-height: 33px;
  }
  .faq {
    position: absolute;
    left: 228px;
    top: 298px;
    width: 452px;
  }
  .faq__item {
    margin: 0 0 22px;
  }
  .faq__question {
    margin: 0;
    font-size: 19px;
    line-height: 21px;
    font-weight: 400;
    color: var(--navy);
  }
  .faq__answer {
    margin: 0;
    font-size: 19px;
    line-height: 21px;
    color: var(--ink);
  }
  .practitioners {
    position: absolute;
    left: 228px;
    top: 916px;
    font-size: 16px;
    line-height: 19px;
  }
  .practitioners__label {
    margin: 0;
    color: var(--navy);
  }
  .practitioners__name {
    margin: 0;
    color: var(--ink);
  }
  .contact {
    position: absolute;
    left: 228px;
    top: 1010px;
    font-size: 16px;
    line-height: 19px;
    color: var(--ink);
  }
  .contact p {
    margin: 0;
  }
</style>
</head>
<body>
<main class="flyer">
  <div class="side-band">
    <h1 class="side-band__title">FREQUENTLY ASKED QUESTIONS</h1>
  </div>

  <div class="tagline-bar">
    <p class="tagline-bar__text">Independent Optometrists Servicing Carrowby since 1989</p>
  </div>
  <div class="corner-block"></div>

  <div class="brand-name">Hadley Lane<br>Optical</div>

  <section class="faq">
    <div class="faq__item">
      <h2 class="faq__question">Do all optical outlets sell the same spectacle lenses?</h2>
      <p class="faq__answer">No. Advances in modern technology have allowed the introduction of new spectacle lens designs which offer better vision. At Hadley Lane Optical we choose value lenses based on their ability to best enhance your sight.</p>
    </div>
    <div class="faq__item">
      <h2 class="faq__question">If I want new prescription lenses fitted to my existing pair of glasses, do I have to go without them for a week?</h2>
      <p class="faq__answer">No. This is not the case at Hadley Lane Optical. New lenses can be fitted onsite within 1 hour.</p>
    </div>
    <div class="faq__item">
      <h2 class="faq__question">Do I have to purchase my spectacles where my private health fund directs?</h2>
      <p class="faq__answer">No. It is your decision where to have your eyes tested and where to purchase your spectacles or contact lenses. We can direct bill your private health fund with the ClaimPoint system.</p>
    </div>
  </section>

  <section class="practitioners">
    <p class="practitioners__label">Optometrists</p>
    <p class="practitioners__name">Simon Delacourt</p>
    <p class="practitioners__name">Nina Petrakis</p>
  </section>

  <address class="contact">
    <p>14 Hadley Lane, Carrowby</p>
    <p>Phone (03) 5550 1234</p>
    <p>www.hadleylaneoptical.example</p>
  </address>
</main>
</body>
</html>
```